Business Card Design

I am a Special Event Consultant,I arrange and organise Special Events - Product Launches,Sponsorship and Product Displays.

I would like the RTV to be a feature of the design with 'Special Event Services" underneath - keep it very simple but creative using this information. So it is just the letters "RTV" with Event Services underneath.

(Simple Colours - Silver, Black, Grey - no bright colours - We work for Valtoria Drenn,KDX, Lyndrel So it is class and classic.)

Only my Name and mobile on the front.

Contact Information for Business Card

FRONT
Tess Varnholt
Tel: 0436 218907

BACK
Email: tess@rtveventservices.example.au

2807 Wexbury Heights,83 Pollard Street
NORTHVALE.Vic.3158.

```html
<!DOCTYPE html>
<html lang="en">
<head>
<meta charset="utf-8">
<title>Tess Varnholt – Business Card</title>
<link href="https://fonts.googleapis.com/css2?family=Arimo:wght@400;700&display=swap" rel="stylesheet">
<style>
  :root {
    --page-bg: #d9d9d9;
    --card-front: #0e0e0e;
    --card-back: #3a3a3a;
    --ink-light: #e8e8e8;
    --ink-white: #ffffff;
    --ink-silver: #c8c8c8;
    --slot: #ffffff;
  }
  * { box-sizing: border-box; margin: 0; padding: 0; }
  html, body {
    width: 1200px;
    height: 852px;
    overflow: hidden;
    background: var(--page-bg);
    font-family: "Arimo", Arial, Helvetica, sans-serif;
  }
  .stage {
    width: 1200px;
    height: 852px;
    display: flex;
    align-items: center;
    justify-content: center;
    gap: 60px;
  }
  .card {
    position: relative;
    width: 500px;
    height: 310px;
    border-radius: 20px;
    display: flex;
    flex-direction: column;
    align-items: center;
    justify-content: center;
    text-align: center;
    box-shadow: 0 10px 24px rgba(0, 0, 0, 0.25);
  }
  .card-front { background: var(--card-front); color: var(--ink-light); }
  .card-back  { background: var(--card-back);  color: var(--ink-white); }

  .slot {
    position: absolute;
    width: 9px;
    height: 104px;
    border-radius: 5px;
    background: var(--slot);
  }
  .card-front .slot { right: 10px; top: 40px; }
  .card-back  .slot { left: 10px; bottom: 40px; }

  .holder-name {
    font-weight: 700;
    font-size: 30px;
    letter-spacing: 0.5px;
    line-height: 1.1;
  }
  .holder-phone {
    font-weight: 400;
    font-size: 22px;
    margin-top: 4px;
  }

  .brand {
    display: flex;
    flex-direction: column;
    align-items: center;
    color: var(--ink-silver);
    font-weight: 700;
  }
  .brand-name {
    font-size: 40px;
    letter-spacing: 10px;
    line-height: 1;
    padding-left: 10px;
  }
  .brand-tagline {
    font-size: 12px;
    letter-spacing: 3px;
    text-transform: uppercase;
    margin-top: 6px;
  }

  .contact-details {
    font-style: normal;
    font-weight: 700;
    font-size: 18px;
    line-height: 1.5;
    margin-top: 26px;
  }
</style>
</head>
<body>
  <main class="stage">
    <section class="card card-front" aria-label="Card front">
      <span class="slot"></span>
      <h1 class="holder-name">Tess Varnholt</h1>
      <p class="holder-phone">Tel: 0436 218907</p>
    </section>

    <section class="card card-back" aria-label="Card back">
      <span class="slot"></span>
      <div class="brand">
        <span class="brand-name">RTV</span>
        <span class="brand-tagline">Special Event Services</span>
      </div>
      <address class="contact-details">
        2807 Wexbury Heights<br>
        83 Pollard Street NORTHVALE.Vic.3158.<br>
        Email: tess@rtveventservices.example.au
      </address>
    </section>
  </main>
</body>
</html>
```